Business Card design for Brightvale Global

we need a business card design for our company. we are a trading company based in LA.

Company Name: Brightvale Global Corp.
Contact: Marcus Ortega
Title: CEO
Tel: 310-647-2093
Email: bvgcorp7@mailnest.example

Target Market(s)

International, especially China

Industry/Entity Type

Trade

Colors
3276b5
34a7d8
0555a3
0493ce
85cae6
85acd3
d0dfed
cee9f5

Requirements
Must have
• Logo and contact, to have international/global feeling

```html
<!DOCTYPE html>
<html lang="en">
<head>
<meta charset="utf-8">
<title>Brightvale Global — Business Card</title>
<link rel="stylesheet" href="https://fonts.googleapis.com/css2?family=Mulish:wght@300;400;700;800&display=swap">
<style>
  :root {
    --bg: #e9ecf0;
    --white: #ffffff;
    --navy: #1b3f77;
    --ink: #17345f;
    --blue: #2f80c6;
    --sky: #34a7d8;
    --band-light: #2a82c9;
    --band-dark: #1d4a8a;
    --text-grey: #2b2b2b;
    --black: #0c0c0c;
    --map-tone: #262626;
  }
  * { margin: 0; padding: 0; box-sizing: border-box; }
  html, body { width: 1200px; height: 844px; overflow: hidden; }
  body {
    background: var(--bg);
    font-family: "Mulish", sans-serif;
    position: relative;
  }
  .card {
    position: absolute;
    top: 272px;
    width: 520px;
    height: 300px;
    border-radius: 4px;
    overflow: hidden;
    box-shadow: 0 6px 20px rgba(0,0,0,0.18);
  }
  /* Front */
  .card-front { left: 50px; background: var(--white); }
  .front-wordmark {
    position: absolute;
    left: 60px;
    top: 52px;
    display: flex;
    align-items: center;
    gap: 12px;
  }
  .wordmark-dot {
    width: 34px; height: 34px;
    border-radius: 50%;
    background: var(--blue);
  }
  .wordmark-text {
    font-weight: 700;
    font-size: 34px;
    color: var(--ink);
    letter-spacing: -0.5px;
  }
  .contact {
    position: absolute;
    right: 34px;
    top: 112px;
    text-align: right;
    font-size: 15px;
    color: var(--text-grey);
    line-height: 1.45;
  }
  .contact-row { display: flex; justify-content: flex-end; align-items: center; gap: 6px; }
  .contact-row svg { width: 12px; height: 12px; fill: var(--ink); }
  .person { position: absolute; left: 36px; top: 196px; }
  .person-name { font-size: 22px; color: var(--blue); font-weight: 400; }
  .person-name .surname { color: var(--ink); font-weight: 700; }
  .person-title { font-size: 11px; color: var(--text-grey); margin-top: 3px; }
  .band-light {
    position: absolute; left: 0; right: 0; bottom: 24px; height: 12px;
    background: var(--band-light);
  }
  .band-dark {
    position: absolute; left: 0; right: 0; bottom: 0; height: 24px;
    background: var(--band-dark);
  }
  /* Back */
  .card-back { left: 630px; background: var(--black); }
  .world-map {
    position: absolute; inset: 0;
    background: radial-gradient(ellipse at 50% 45%, var(--map-tone) 0%, var(--black) 75%);
  }
  .back-wordmark {
    position: absolute;
    inset: 0;
    display: flex;
    align-items: center;
    justify-content: center;
    gap: 12px;
  }
  .back-wordmark .wordmark-dot { background: var(--white); }
  .back-wordmark .wordmark-text { color: var(--white); }
</style>
</head>
<body>
  <section class="card card-front" aria-label="Business card front">
    <div class="front-wordmark">
      <span class="wordmark-dot"></span>
      <span class="wordmark-text">Brightvale Global</span>
    </div>
    <div class="contact">
      <div class="contact-row">310-647-2093
        <svg viewBox="0 0 24 24" aria-hidden="true"><path d="M6.6 10.8a15 15 0 0 0 6.6 6.6l2.2-2.2a1 1 0 0 1 1-.25 11.4 11.4 0 0 0 3.6.57 1 1 0 0 1 1 1V20a1 1 0 0 1-1 1A17 17 0 0 1 3 4a1 1 0 0 1 1-1h3.5a1 1 0 0 1 1 1c0 1.25.2 2.45.57 3.57a1 1 0 0 1-.25 1z"/></svg>
      </div>
      <div class="contact-row">bvgcorp7@mailnest.example
        <svg viewBox="0 0 24 24" aria-hidden="true"><path d="M2 5h20v14H2z M3 6l9 7 9-7" fill="none" stroke="#17345f" stroke-width="2"/></svg>
      </div>
    </div>
    <div class="person">
      <div class="person-name">Marcus <span class="surname">Ortega</span></div>
      <div class="person-title">CEO</div>
    </div>
    <div class="band-light"></div>
    <div class="band-dark"></div>
  </section>

  <section class="card card-back" aria-label="Business card back">
    <div class="world-map" role="img" aria-label="Faint world map in dark grey across the card"></div>
    <div class="back-wordmark">
      <span class="wordmark-dot"></span>
      <span class="wordmark-text">Brightvale Global</span>
    </div>
  </section>
</body>
</html>
```